Design some Business Cards for CFBA

Wording for business cards:

Company: Coastline Freight Brokers Alliance
Name: Desmond Harlow
Job Title: Network Development Executive
email: desmond@[login to view URL]
Tel/Mob: Mobile: +001 555-274-9160
Skype: [login to view URL]
Address: 4187 SW 63rd Ct; Ste 240, Miami FL 33165, USA
website: [login to view URL]

```html
<!DOCTYPE html>
<html lang="en">
<head>
<meta charset="utf-8">
<title>CFBA Business Cards</title>
<link rel="stylesheet" href="https://fonts.googleapis.com/css2?family=Arimo:wght@400;700&display=swap">
<style>
  :root {
    --backdrop: #5b5b59;
    --card-blue-light: #8aa0c0;
    --card-blue-dark: #3d5376;
    --band-light: #a9bcd6;
    --band-dark: #5f7799;
    --paper: #f4f2ed;
    --navy: #2f2a80;
    --rule-red: #c0262c;
    --white: #ffffff;
    --ink-dark: #1e2340;
  }
  * { box-sizing: border-box; margin: 0; padding: 0; }
  html, body { width: 1200px; height: 780px; overflow: hidden; }
  body {
    background: var(--backdrop);
    font-family: "Arimo", Arial, sans-serif;
    position: relative;
  }
  .card {
    position: absolute;
    width: 560px;
    height: 320px;
    box-shadow: 0 8px 22px rgba(0,0,0,0.45);
    overflow: hidden;
  }
  /* Front card */
  .card-front {
    left: 60px; top: 70px;
    background: radial-gradient(ellipse at 45% 40%, var(--card-blue-light) 0%, var(--card-blue-dark) 100%);
  }
  .front-panel {
    position: absolute;
    left: 40px; right: 0; top: 78px; height: 130px;
    background: var(--white);
    border: 3px solid var(--rule-red);
    border-right: none;
    display: flex; align-items: center;
    padding-left: 60px; gap: 26px;
  }
  .brand-dot {
    width: 74px; height: 74px; border-radius: 50%;
    background: #c9d3e4;
    flex: none;
  }
  .brand-block { display: flex; flex-direction: column; }
  .brand-name {
    font-weight: 700; color: var(--navy);
    font-size: 64px; letter-spacing: 4px; line-height: 1;
  }
  .brand-tagline {
    font-weight: 700; color: var(--navy);
    font-size: 11px; letter-spacing: 0.6px; text-transform: uppercase;
    margin-top: 8px;
  }
  .front-web {
    position: absolute; left: 0; right: 0; top: 226px;
    text-align: center; padding-left: 160px;
    color: var(--white); font-weight: 700; font-size: 17px;
  }
  /* Back card */
  .card-back {
    left: 590px; top: 410px;
    background: var(--paper);
  }
  .info-band {
    position: absolute; left: 0; right: 0; top: 108px; height: 100px;
    background: linear-gradient(90deg, var(--band-dark) 0%, var(--band-light) 55%, var(--band-dark) 100%);
  }
  .person {
    position: absolute; left: 0; top: 108px; width: 318px; height: 100px;
  }
  .person-name {
    position: absolute; left: 28px; top: 20px;
    color: var(--white); font-weight: 700; font-size: 36px; letter-spacing: -0.5px;
    white-space: nowrap;
  }
  .person-title {
    position: absolute; left: 0; top: 68px; width: 318px; height: 26px;
    background: var(--band-light);
    color: var(--navy); font-weight: 700; font-size: 14px;
    padding: 5px 0 0 28px;
  }
  .contact-list {
    position: absolute; left: 318px; top: 108px; width: 242px; height: 100px;
    border-left: 2px solid rgba(255,255,255,0.7);
    list-style: none;
    padding: 6px 0 0 12px;
  }
  .contact-list li {
    display: flex; align-items: center; gap: 10px;
    height: 22px;
    color: var(--white); font-size: 11px;
  }
  .contact-list svg { width: 15px; height: 15px; flex: none; }
  .address {
    position: absolute; left: 0; right: 0; top: 218px;
    text-align: center; color: var(--ink-dark);
    font-weight: 700; font-size: 14px;
  }
  .back-brand {
    position: absolute; left: 0; right: 0; top: 244px;
    display: flex; flex-direction: column; align-items: center;
  }
  .back-brand .brand-name { font-size: 44px; letter-spacing: 3px; }
  .back-brand .brand-tagline { font-size: 8px; margin-top: 5px; }
</style>
</head>
<body>

  <section class="card card-front" aria-label="Card front">
    <div class="front-panel">
      <div class="brand-dot"></div>
      <div class="brand-block">
        <span class="brand-name">CFBA</span>
        <span class="brand-tagline">Coastline Freight Brokers Alliance</span>
      </div>
    </div>
    <p class="front-web">www.GO2cfba.com</p>
  </section>

  <section class="card card-back" aria-label="Card back">
    <div class="info-band"></div>
    <div class="person">
      <h1 class="person-name">Desmond Harlow</h1>
      <p class="person-title">Network Development Executive</p>
    </div>
    <ul class="contact-list">
      <li>
        <svg viewBox="0 0 16 16" aria-hidden="true"><rect x="4" y="1" width="8" height="14" rx="1.5" fill="none" stroke="#fff" stroke-width="1.5"/><circle cx="8" cy="12.5" r="0.9" fill="#fff"/></svg>
        +001 555-274-9160
      </li>
      <li>
        <svg viewBox="0 0 16 16" aria-hidden="true"><circle cx="8" cy="8" r="6.5" fill="none" stroke="#fff" stroke-width="1.4"/><ellipse cx="8" cy="8" rx="2.8" ry="6.5" fill="none" stroke="#fff" stroke-width="1.1"/><line x1="1.5" y1="8" x2="14.5" y2="8" stroke="#fff" stroke-width="1.1"/></svg>
        www.GO2cfba.com
      </li>
      <li>
        <svg viewBox="0 0 16 16" aria-hidden="true"><rect x="1.5" y="3.5" width="13" height="9" fill="none" stroke="#fff" stroke-width="1.4"/><polyline points="1.5,3.5 8,9 14.5,3.5" fill="none" stroke="#fff" stroke-width="1.4"/></svg>
        desmond@go2cfba.com
      </li>
      <li>
        <svg viewBox="0 0 16 16" aria-hidden="true"><circle cx="8" cy="8" r="6.5" fill="none" stroke="#fff" stroke-width="1.4"/></svg>
        Desmond.Harlow
      </li>
    </ul>
    <p class="address">4187 SW 63rd Ct; Ste 240, Miami FL 33165, USA</p>
    <div class="back-brand">
      <span class="brand-name">CFBA</span>
      <span class="brand-tagline">Coastline Freight Brokers Alliance</span>
    </div>
  </section>

</body>
</html>
```